Kestrel Photography Business Card

I need a business card designed for a photography business based in Perth, Western Australia called Kestrel Photography.

We specialise in wedding, event photography and portrait photography.

The business card must borrow the style of the attached logo.

The hex codes for the colours in the logo are:
#ED1D85 - Pink
#89C23E - Green
#37282F - Black

The name on the card will be:
Name: Toviran
Phone: 0417395268
Website: www.kestrelphotography.com.au
Linkloop: kestrelphotography

I am open and happy to accept creative concepts.

I’d like some space at the back for writing notes and appointment details.

```html
<!DOCTYPE html>
<html lang="en">
<head>
<meta charset="utf-8">
<title>Kestrel Photography – Business Card</title>
<link href="https://fonts.googleapis.com/css2?family=Tenor+Sans&display=swap" rel="stylesheet">
<style>
  :root {
    --pink: #ED1D85;
    --green: #89C23E;
    --band: #A6CA45;
    --black: #37282F;
    --white: #ffffff;
    --stage: #ececec;
    --font: "Tenor Sans", "Helvetica Neue", Arial, sans-serif;
  }
  * { margin: 0; padding: 0; box-sizing: border-box; }
  html, body {
    width: 1200px; height: 1000px; overflow: hidden;
    background: var(--stage);
    font-family: var(--font);
  }
  .card {
    position: absolute; left: 220px;
    width: 760px; height: 456px;
    background: var(--white);
    overflow: hidden;
    box-shadow: 0 2px 8px rgba(0,0,0,0.15);
  }
  .card--front { top: 29px; }
  .card--back  { top: 515px; }

  .decor {
    position: absolute;
  }
  .decor--front-left {
    left: 0; top: 0; width: 220px; height: 240px;
    background: radial-gradient(circle at 20% 25%, rgba(237,29,133,0.18), rgba(137,194,62,0.10) 55%, rgba(255,255,255,0) 75%);
  }
  .decor--front-right {
    right: 0; top: 0; width: 240px; height: 366px;
    background: radial-gradient(circle at 85% 50%, rgba(137,194,62,0.14), rgba(237,29,133,0.18) 45%, rgba(255,255,255,0) 78%);
  }
  .decor--back-right {
    right: 0; top: 0; width: 260px; height: 366px;
    background: radial-gradient(circle at 85% 50%, rgba(137,194,62,0.14), rgba(237,29,133,0.18) 45%, rgba(255,255,255,0) 78%);
  }

  .brand-mark {
    position: absolute;
    display: flex; align-items: center; gap: 14px;
  }
  .brand-mark__dot {
    width: 58px; height: 58px; border-radius: 50%;
    background: var(--pink);
  }
  .brand-mark__name {
    color: var(--black); font-size: 26px; letter-spacing: 4px;
    text-transform: uppercase;
  }
  .card--front .brand-mark { left: 0; right: 0; top: 95px; justify-content: center; }
  .card--back .brand-mark { left: 30px; top: 125px; gap: 10px; }
  .card--back .brand-mark__dot { width: 44px; height: 44px; }
  .card--back .brand-mark__name { font-size: 22px; letter-spacing: 3px; }

  .business-name {
    position: absolute; left: 0; right: 0; top: 250px;
    text-align: center; color: var(--black);
    font-size: 25px; letter-spacing: 13px; text-transform: uppercase;
  }
  .contact {
    position: absolute; left: 0; right: 0; top: 305px;
    display: flex; justify-content: center; align-items: center; gap: 26px;
    color: var(--pink); font-size: 26px; letter-spacing: 4px;
    text-transform: uppercase;
  }
  .contact__phone { display: flex; align-items: center; gap: 8px; }
  .contact__icon { width: 28px; height: 28px; }

  .band {
    position: absolute; left: 0; right: 0; bottom: 0; height: 90px;
    background: var(--band);
    color: var(--white); text-transform: uppercase;
  }
  .band__web {
    position: absolute; left: 0; right: 0; top: 20px;
    text-align: center; font-size: 24px; letter-spacing: 5px;
  }
  .band__social {
    position: absolute; left: 0; right: 0; top: 58px;
    text-align: center; font-size: 16px; letter-spacing: 4px;
  }
  .band--back .band__tagline {
    position: absolute; right: 32px; top: 18px;
    font-size: 17px; letter-spacing: 4px;
  }
  .band--back .band__web {
    left: auto; right: 32px; top: 46px; text-align: right;
  }

  .field-label {
    position: absolute; left: 250px;
    color: var(--pink); font-size: 22px; letter-spacing: 4px;
    text-transform: uppercase;
  }
  .field-label--appointment { top: 50px; }
  .field-label--notes { top: 195px; }
  .write-line {
    position: absolute; left: 250px; width: 480px; height: 0;
    border-bottom: 2px dotted var(--green);
  }
</style>
</head>
<body>

<section class="card card--front" aria-label="Business card front">
  <div class="decor decor--front-left" role="img" aria-label="Faint petal ring decoration"></div>
  <div class="decor decor--front-right" role="img" aria-label="Faint petal ring decoration"></div>

  <div class="brand-mark">
    <span class="brand-mark__dot"></span>
    <span class="brand-mark__name">Kestrel</span>
  </div>

  <h1 class="business-name">Kestrel Photography</h1>

  <div class="contact">
    <span class="contact__name">Toviran</span>
    <span class="contact__phone">
      <svg class="contact__icon" viewBox="0 0 28 28" aria-hidden="true">
        <circle cx="14" cy="14" r="14" fill="var(--green)"/>
        <path d="M10 7c1 0 2 2.5 2 3.5s-1.3 1.3-1.3 2 3 4.8 4 5 1.2-1.3 2-1.3 3.3 1 3.3 2-1.5 2.5-3 2.5C12 20.7 7 15 7 11c0-2 2-4 3-4z" fill="var(--white)"/>
      </svg>
      0417395268
    </span>
  </div>

  <footer class="band">
    <div class="band__web">www.kestrelphotography.com.au</div>
    <div class="band__social">Linkloop: kestrelphotography</div>
  </footer>
</section>

<section class="card card--back" aria-label="Business card back">
  <div class="decor decor--back-right" role="img" aria-label="Faint petal ring decoration"></div>

  <div class="brand-mark">
    <span class="brand-mark__dot"></span>
    <span class="brand-mark__name">Kestrel</span>
  </div>

  <div class="field-label field-label--appointment">Appointment</div>
  <div class="write-line" style="top:110px"></div>
  <div class="write-line" style="top:150px"></div>

  <div class="field-label field-label--notes">Notes</div>
  <div class="write-line" style="top:255px"></div>
  <div class="write-line" style="top:292px"></div>
  <div class="write-line" style="top:329px"></div>

  <footer class="band band--back">
    <div class="band__tagline">Wedding, Event &amp; Portrait Photography</div>
    <div class="band__web">www.kestrelphotography.com.au</div>
  </footer>
</section>

</body>
</html>
```